Construction Company Business Card

Business Card Design using new Logo

Contact Information for Business Card

include all company info and website

Requirements
Must have
• Wesley Corman - President
ph. 254-617-0382
Cedar Knoll, TX
wesley@ironmarkframing.com
www.ironmarkframing.com

```html
<!DOCTYPE html>
<html lang="en">
<head>
<meta charset="utf-8">
<title>Ironmark Framing – Business Card</title>
<link href="https://fonts.googleapis.com/css2?family=Montserrat:wght@400;500;700&display=swap" rel="stylesheet">
<style>
  :root {
    --backdrop: #efefef;
    --card: #2a2928;
    --ink: #cfcfcf;
    --ink-soft: #bdbdbd;
    --accent: #d2232a;
    --card-shadow: 0 6px 18px rgba(0,0,0,0.18);
  }
  * { box-sizing: border-box; margin: 0; padding: 0; }
  html, body {
    width: 1200px;
    height: 900px;
    overflow: hidden;
    background: var(--backdrop);
    font-family: "Montserrat", sans-serif;
  }
  .canvas {
    position: relative;
    width: 1200px;
    height: 900px;
  }
  .card {
    position: absolute;
    width: 560px;
    height: 320px;
    background: var(--card);
    box-shadow: var(--card-shadow);
    color: var(--ink);
  }
  .card--front { left: 80px; top: 110px; }
  .card--back  { left: 560px; top: 470px; }

  .wordmark {
    display: flex;
    align-items: center;
    gap: 14px;
    font-weight: 500;
    text-transform: uppercase;
    color: var(--ink);
    letter-spacing: 0.06em;
  }
  .wordmark__mark {
    width: 14px;
    height: 14px;
    background: var(--accent);
    flex: none;
  }
  .card--front .wordmark {
    position: absolute;
    left: 0; right: 0; top: 0; bottom: 0;
    justify-content: center;
    font-size: 34px;
  }
  .card--back .wordmark {
    position: absolute;
    left: 120px;
    top: 78px;
    font-size: 22px;
    gap: 10px;
  }
  .card--back .wordmark__mark { width: 10px; height: 10px; }

  .holder {
    position: absolute;
    left: 40px;
    top: 186px;
  }
  .holder__name {
    font-weight: 700;
    font-size: 19px;
    letter-spacing: 0.02em;
    color: var(--ink);
    text-transform: uppercase;
  }
  .holder__role {
    display: inline-block;
    margin-top: 4px;
    padding: 2px 8px;
    background: var(--accent);
    color: #f2d6d6;
    font-size: 14px;
    font-weight: 400;
    letter-spacing: 0.03em;
    text-transform: uppercase;
  }

  .contact {
    position: absolute;
    right: 36px;
    bottom: 34px;
    text-align: right;
    font-size: 14px;
    line-height: 1.45;
    color: var(--ink-soft);
  }
  .contact__location {
    margin-top: 10px;
    font-weight: 700;
    color: var(--ink);
    display: flex;
    align-items: center;
    justify-content: flex-end;
    gap: 8px;
  }
  .contact__bar {
    width: 4px;
    height: 14px;
    background: var(--accent);
  }
</style>
</head>
<body>
  <main class="canvas">
    <section class="card card--front" aria-label="Business card front">
      <div class="wordmark">
        <span class="wordmark__mark"></span>
        <span class="wordmark__name">Ironmark Framing</span>
      </div>
    </section>

    <section class="card card--back" aria-label="Business card back">
      <div class="wordmark">
        <span class="wordmark__mark"></span>
        <span class="wordmark__name">Ironmark Framing</span>
      </div>

      <div class="holder">
        <p class="holder__name">Wesley Corman</p>
        <p class="holder__role">President</p>
      </div>

      <div class="contact">
        <p class="contact__phone">254-617-0382</p>
        <p class="contact__email">wesley@ironmarkframing.com</p>
        <p class="contact__web">www.ironmarkframing.com</p>
        <p class="contact__location">Cedar Knoll, TX <span class="contact__bar"></span></p>
      </div>
    </section>
  </main>
</body>
</html>
```